Redesign my business cards

I would like pretty much all the same information as my current business cards but redesigned to stand out more and be more unique photo uploaded to show my current business cards don’t mind if you want to remove or replace I for on the back

```html
<!DOCTYPE html>
<html lang="en">
<head>
<meta charset="utf-8">
<title>Halvern Detailing – Business Card</title>
<link rel="stylesheet" href="https://fonts.googleapis.com/css2?family=Montserrat:wght@400;500;700&display=swap">
<style>
  :root {
    --stage: #17748a;
    --card: #062a3c;
    --accent: #3cbfe2;
    --art: #2f8dab;
    --art-deep: #267a96;
    --wave: #2a7a91;
    --ink: #ffffff;
    --body-ink: #dbe9ef;
  }
  * { margin: 0; padding: 0; box-sizing: border-box; }
  html, body { width: 886px; height: 1200px; overflow: hidden; }
  body {
    background: var(--stage);
    font-family: "Montserrat", sans-serif;
    position: relative;
  }
  .card-slot {
    position: absolute;
    left: 63px;
    width: 760px;
    height: 434px;
    box-shadow: 0 18px 40px rgba(0, 30, 45, 0.35);
  }
  .card-slot--front { top: 120px; }
  .card-slot--back { top: 646px; }
  .card {
    position: absolute;
    top: 0; left: 0;
    width: 687px;
    height: 392px;
    background: var(--card);
    overflow: hidden;
    transform: scale(1.1063);
    transform-origin: 0 0;
  }
  .card-art {
    position: absolute;
    top: 0; left: 0;
    width: 687px;
    height: 392px;
  }

  /* Front */
  .brand { position: absolute; left: 42px; top: 40px; display: flex; align-items: center; gap: 22px; }
  .brand-mark { width: 86px; height: 86px; border-radius: 50%; background: var(--accent); }
  .brand-name { color: var(--accent); font-weight: 700; font-size: 33px; letter-spacing: 0.5px; line-height: 1; }
  .brand-sub { color: var(--ink); font-weight: 500; font-size: 13.5px; letter-spacing: 4px; margin-top: 6px; }
  .person { position: absolute; left: 46px; top: 210px; }
  .person-name { color: var(--accent); font-weight: 500; font-size: 24px; letter-spacing: 0.3px; line-height: 1; }
  .person-role { color: var(--ink); font-size: 13px; margin-top: 4px; }
  .contact { position: absolute; left: 46px; top: 286px; list-style: none; }
  .contact li { display: flex; align-items: center; gap: 13px; color: var(--accent); font-size: 15px; height: 24px; margin-bottom: 9px; }
  .contact svg { width: 22px; height: 22px; flex: none; }

  /* Back */
  .service { position: absolute; width: 240px; }
  .service--interior { left: 47px; top: 45px; }
  .service--exterior { left: 47px; top: 199px; }
  .service--full { left: 329px; top: 45px; }
  .service-title { color: var(--accent); font-weight: 500; font-size: 18px; letter-spacing: 0.2px; margin-bottom: 6px; }
  .service-text { color: var(--body-ink); font-size: 13.2px; line-height: 16.4px; }
  .price {
    display: inline-block; margin-top: 12px;
    background: var(--accent); color: var(--ink);
    font-size: 10.5px; font-weight: 500;
    padding: 2px 10px; border-radius: 3px;
  }
</style>
</head>
<body>

<div class="card-slot card-slot--front">
  <section class="card card--front">
    <svg class="card-art" viewBox="0 0 687 392" role="img" aria-label="Illustration of a car front bursting through a water splash">
      <path d="M470 0 H687 V392 H505 C470 360 450 320 458 280 C440 250 450 210 470 190 C448 160 445 110 462 80 C450 50 455 20 470 0 Z" fill="var(--art)"/>
    </svg>
    <div class="brand">
      <span class="brand-mark" aria-hidden="true"></span>
      <div>
        <div class="brand-name">HALVERN</div>
        <div class="brand-sub">DETAILING</div>
      </div>
    </div>
    <div class="person">
      <h1 class="person-name">OWEN MARLOW</h1>
      <p class="person-role">OWNER / OPERATOR</p>
    </div>
    <ul class="contact">
      <li>
        <svg viewBox="0 0 22 22" aria-hidden="true"><circle cx="11" cy="11" r="10.5" fill="#fff"/><rect x="7.5" y="4.5" width="7" height="13" rx="1.5" fill="var(--card)"/></svg>
        0491570006
      </li>
      <li>
        <svg viewBox="0 0 22 22" aria-hidden="true"><circle cx="11" cy="11" r="10.5" fill="#fff"/><rect x="5.5" y="7" width="11" height="8" rx="1" fill="var(--card)"/><path d="M5.8 7.5 L11 11.5 L16.2 7.5" stroke="#fff" stroke-width="1.2" fill="none"/></svg>
        HALVERNDETAILING@MAILBOX.COM
      </li>
    </ul>
  </section>
</div>

<div class="card-slot card-slot--back">
  <section class="card card--back">
    <svg class="card-art" viewBox="0 0 687 392" aria-hidden="true">
      <path d="M0 343 C60 330 110 352 180 352 C260 352 320 322 380 360 C395 370 402 382 405 392 H0 Z" fill="var(--wave)"/>
    </svg>
    <svg class="card-art" viewBox="0 0 687 392" role="img" aria-label="Illustration of a car rear emerging from a water splash">
      <path d="M687 182 V392 H440 C420 360 410 320 425 290 C415 260 430 225 460 215 C500 200 540 192 580 186 C620 180 650 178 687 182 Z" fill="var(--art)"/>
    </svg>

    <article class="service service--interior">
      <h2 class="service-title">INTERIOR DETAIL</h2>
      <p class="service-text">Vacume &amp; deep clean of carpets &amp; upholstery or leather treatment, interior trim clean &amp; condition, window polish and treatment, steam clean and stain removal</p>
      <span class="price">$150</span>
    </article>
    <article class="service service--exterior">
      <h2 class="service-title">EXTERIOR DETAIL</h2>
      <p class="service-text">Extreme wash &amp; polish, exterior trim reviver &amp; protector window polish &amp; treatment, tyre dressing, engine bay cleaned</p>
      <span class="price">$250</span>
    </article>
    <article class="service service--full">
      <h2 class="service-title">FULL EXTREME DETAIL</h2>
      <p class="service-text">Extreme wash &amp; polish, tyre dressing, engine bay cleaned, vacume &amp; deep clean of carpets &amp; upholstery or lether treatment, interior &amp; exterior trim reviver &amp; protector, window polish and treatment</p>
      <span class="price">$350</span>
    </article>
  </section>
</div>

</body>
</html>
```